TAVRO Capital Group LLC a High Risk Big Rewards company for Rich Young Entrepreneurs

We would like a very modern, powerful in the eyes of our customers, modern, minimalist feel, financial gain. this business card is for young Rich entrepreneurs who want to invest money into High Risk, Big Rewards Businesses. The card Should sell the business!! let your creativity go Wild! I pick most of the designers for this project because of your BOLD Designs, I would like this card to be Bold, Modern, Minimalist, use as many effects in your graphic Artist Mind, Do not let the Financial sound of this business to make you think Conservative that's the last thing we are! if you have a lot of money and you want to play a risky market call US
Updates

Project Deadline Extended
Reason: have not received, enough designs to choose 1st and second place, sure I have received over 100 designs but it seems most designers are submitting every card they have ever made before and calling it mine, please we are looking for fresh ideas please!

Target Market(s)

Private Risky Investors

Industry/Entity Type

Financial

Contact Information for Business Card

powerful in the eyes of our customers,modern, minimalist feel

Font styles to use
Other font styles liked:
• Modern feeling fonts

Requirements
Must have
• The Company Name is TAVRO Capital Group LLC and it must be on the CARD
• My Name, title, Cell , email
• Delvin Ashcroft G.E.D.
• Managing Member
• 555.038.6195
• delvin@tavrocapitalgroup.example
Nice to have
• try a black thick plastic card with round corners with Delvin Ashcroft GED (make sure GED is smaller than name) just on one side of the card, and my phone number with out the icons and email on the other side, this card should look like a exclusive credit card or exclusive VIP card, something you would never loose

```html
<!DOCTYPE html>
<html lang="en">
<head>
<meta charset="utf-8">
<title>TAVRO Capital Group LLC — Business Card</title>
<link rel="stylesheet" href="https://fonts.googleapis.com/css2?family=Bebas+Neue&display=swap">
<style>
  :root {
    --backdrop: #45423f;
    --card-black: #2a2a2c;
    --accent-blue: #35c6ee;
    --ink-dark: #1e1e20;
  }
  html, body {
    margin: 0;
    padding: 0;
    width: 1200px;
    height: 1000px;
    overflow: hidden;
    background: var(--backdrop);
  }
  .canvas {
    position: relative;
    width: 1200px;
    height: 1000px;
  }
  .card {
    position: absolute;
    left: 220px;
    width: 760px;
    height: 434px;
    display: block;
    box-shadow: 0 10px 30px rgba(0,0,0,0.35);
  }
  .card--contact { top: 46px; }
  .card--brand { top: 520px; }
  .card-face { fill: var(--card-black); }
  .accent { fill: var(--accent-blue); }
  .company-name {
    font-family: "Bebas Neue", sans-serif;
    fill: var(--accent-blue);
    letter-spacing: 0.5px;
  }
  .company-tagline {
    font-family: "Bebas Neue", sans-serif;
    fill: var(--accent-blue);
    letter-spacing: 0.5px;
  }
  .contact-line {
    font-family: "Bebas Neue", sans-serif;
    fill: var(--ink-dark);
    letter-spacing: 0.6px;
  }
</style>
</head>
<body>
<main class="canvas">

  <!-- Contact side -->
  <svg class="card card--contact" viewBox="0 0 760 434" aria-label="TAVRO Capital Group LLC business card, contact side">
    <rect class="card-face" x="0" y="0" width="760" height="434"/>
    <polygon class="accent" points="455,0 700,0 455,72"/>
    <rect class="accent" x="470" y="160" width="290" height="274"/>
    <rect class="accent" x="40" y="150" width="430" height="17"/>

    <text class="company-name" x="58" y="118" font-size="50">TAVRO CAPITAL GROUP LLC</text>
    <text class="company-tagline" x="455" y="143" font-size="23" text-anchor="end">A DOMESTIC LIMITED LIABILITY COMPANY</text>

    <text class="contact-line" x="486" y="192" font-size="19">DELVIN@TAVROCAPITALGROUP.EXAMPLE</text>
    <text class="contact-line" x="486" y="222" font-size="26">DELVIN ASHCROFT G.E.D</text>
    <text class="contact-line" x="486" y="248" font-size="19">MANAGING MEMBER</text>
    <text class="contact-line" x="486" y="274" font-size="19">555.038.6195</text>
  </svg>

  <!-- Brand side -->
  <svg class="card card--brand" viewBox="0 0 760 434" aria-label="TAVRO Capital Group LLC business card, brand side">
    <rect class="card-face" x="0" y="0" width="760" height="434"/>
    <g class="brand-lockup" transform="translate(70 330) rotate(-17)">
      <rect class="accent" x="0" y="-44" width="34" height="24"/>
      <text class="company-name" x="40" y="0" font-size="52">TAVRO CAPITAL GROUP LLC</text>
      <text class="company-tagline" x="92" y="24" font-size="23">A DOMESTIC LIMITED LIABILITY COMPANY</text>
      <rect class="accent" x="470" y="-62" width="170" height="18"/>
    </g>
  </svg>

</main>
</body>
</html>
```